Etiketten-Design für Kräuterbonbon-Metalldose
Marlene Vosk hat sehr viel Talent. Das Design ist absolut kreativ.
Zielgruppe
Unsere Firma VelbraCor verkauft verschiedene Sorten Kräuterbonbons.
Wir brauchen ein Etikett, dass auf eine Metall-Dose (Durchmesser 10 cam, Höhe ca. 3 cm) geklebt wird.
Zielgruppe: jung-alt
Aufgabenstellung
Der Name unserer Kräuterbonbons ist Pfeffling.
Wir möchten, dass unsere Kunden, wenn sie das Etikett sehen einen Bezug zur Schweiz herstellen können.
Wir verwenden für unsere Bonbons unterschiedliche Kräuter für verschiedene Anwendungen:
Konkret sind erstmal 4 Dosen geplant:
-Kräutermischung aus 16 Kräuter gegen Husten
-Salbei gegen Halsschmerzen
-Anis gegen Magenschmerzen
-Zitrone/Ingwer für die Nerven
Vorderseite: Produktbeschreibung
Rückseite: unsere Herstellerangaben
Größenangaben der Dose: Durchmesser 10 cm, Höhe ca. 3 cm
Im Anhang habe ich Ihnen noch weitere/ genauere Informationen zur Verfügung bereitgestellt!

```html
<!DOCTYPE html>
<html lang="de">
<head>
<meta charset="utf-8">
<title>Pfeffling – Dosenetiketten</title>
<link rel="stylesheet" href="https://fonts.googleapis.com/css2?family=Alegreya:wght@400;800&display=swap">
<style>
  :root {
    --page: #ffffff;
    --white: #ffffff;
    --swiss-red: #e2302b;
    --title-red: #d9262b;
  }
  html, body {
    margin: 0;
    padding: 0;
    width: 1200px;
    height: 849px;
    overflow: hidden;
    background: var(--page);
  }
  .sheet { position: relative; width: 1200px; height: 849px; }
  .label { position: absolute; width: 366px; height: 366px; }
  .label svg { display: block; width: 366px; height: 366px; }
  .label--herbs { left: 151px; top: 33px;  --ring: #0b6a35; --ribbon: #0f8a40; --ribbon-dark: #0a6a30; }
  .label--lemon { left: 677px; top: 33px;  --ring: #65227f; --ribbon: #7e2a8e; --ribbon-dark: #5a1d6a; }
  .label--anise { left: 151px; top: 445px; --ring: #b84d2b; --ribbon: #d8672a; --ribbon-dark: #c2542a; }
  .label--sage  { left: 677px; top: 445px; --ring: #ee8b3b; --ribbon: #f4a42e; --ribbon-dark: #ee9430; }

  .ring { fill: none; stroke: var(--ring); stroke-width: 9; }
  .ribbon-band { fill: var(--ribbon); stroke: var(--white); stroke-width: 2; }
  .ribbon-tail { fill: var(--ribbon-dark); stroke: var(--white); stroke-width: 1.5; }
  .brand-name {
    font-family: "Alegreya", serif;
    font-weight: 800;
    font-size: 36px;
    fill: var(--title-red);
    stroke: var(--white);
    stroke-width: 3px;
    paint-order: stroke;
  }
  .variety {
    font-family: "Alegreya", serif;
    font-weight: 400;
    font-size: 10px;
    letter-spacing: 1.8px;
    fill: var(--white);
  }
  .claim {
    font-family: "Alegreya", serif;
    font-weight: 400;
    font-size: 8px;
    letter-spacing: 2px;
    fill: var(--white);
  }
</style>
</head>
<body>
<main class="sheet">
  <svg width="0" height="0" style="position:absolute" aria-hidden="true">
    <defs>
      <clipPath id="label-clip"><circle r="175"/></clipPath>
      <linearGradient id="sky-meadow" x1="0" y1="0" x2="0" y2="1">
        <stop offset="0" stop-color="#8fcfd8"/>
        <stop offset="0.45" stop-color="#c9e6ea"/>
        <stop offset="0.68" stop-color="#a9b0b2"/>
        <stop offset="0.8" stop-color="#8cc63f"/>
        <stop offset="0.88" stop-color="#3fb0e0"/>
        <stop offset="1" stop-color="#4aa83e"/>
      </linearGradient>
      <linearGradient id="red-band" x1="0" y1="0" x2="1" y2="0">
        <stop offset="0" stop-color="#cf2327"/>
        <stop offset="0.5" stop-color="#e2302b"/>
        <stop offset="1" stop-color="#cf2327"/>
      </linearGradient>
      <linearGradient id="flora-herbs" x1="0" y1="0" x2="1" y2="0">
        <stop offset="0" stop-color="#f2d21c" stop-opacity="0.85"/>
        <stop offset="0.2" stop-color="#6f45a8" stop-opacity="0.75"/>
        <stop offset="0.42" stop-color="#ffffff" stop-opacity="0.5"/>
        <stop offset="0.5" stop-color="#9aa0a3" stop-opacity="0.2"/>
        <stop offset="0.58" stop-color="#ffffff" stop-opacity="0.5"/>
        <stop offset="0.8" stop-color="#6f45a8" stop-opacity="0.75"/>
        <stop offset="1" stop-color="#f2d21c" stop-opacity="0.85"/>
      </linearGradient>
      <linearGradient id="flora-lemon" x1="0" y1="0" x2="1" y2="0">
        <stop offset="0" stop-color="#ffe01a" stop-opacity="0.95"/>
        <stop offset="0.2" stop-color="#9cc92a" stop-opacity="0.8"/>
        <stop offset="0.35" stop-color="#1f8a3c" stop-opacity="0.6"/>
        <stop offset="0.5" stop-color="#9aa0a3" stop-opacity="0.15"/>
        <stop offset="0.65" stop-color="#1f8a3c" stop-opacity="0.6"/>
        <stop offset="0.8" stop-color="#9cc92a" stop-opacity="0.8"/>
        <stop offset="1" stop-color="#ffe01a" stop-opacity="0.95"/>
      </linearGradient>
      <linearGradient id="flora-anise" x1="0" y1="0" x2="1" y2="0">
        <stop offset="0" stop-color="#ffffff" stop-opacity="0.7"/>
        <stop offset="0.25" stop-color="#5fb848" stop-opacity="0.55"/>
        <stop offset="0.5" stop-color="#9aa0a3" stop-opacity="0.15"/>
        <stop offset="0.75" stop-color="#5fb848" stop-opacity="0.55"/>
        <stop offset="1" stop-color="#ffffff" stop-opacity="0.7"/>
      </linearGradient>
      <linearGradient id="flora-sage" x1="0" y1="0" x2="1" y2="0">
        <stop offset="0" stop-color="#6a3fa6" stop-opacity="0.85"/>
        <stop offset="0.3" stop-color="#8a62c2" stop-opacity="0.65"/>
        <stop offset="0.5" stop-color="#9aa0a3" stop-opacity="0.15"/>
        <stop offset="0.7" stop-color="#8a62c2" stop-opacity="0.65"/>
        <stop offset="1" stop-color="#6a3fa6" stop-opacity="0.85"/>
      </linearGradient>
      <linearGradient id="flora-fade" x1="0" y1="0" x2="0" y2="1">
        <stop offset="0" stop-color="#fff" stop-opacity="0"/>
        <stop offset="0.3" stop-color="#fff" stop-opacity="1"/>
        <stop offset="1" stop-color="#fff" stop-opacity="1"/>
      </linearGradient>
      <mask id="flora-mask"><rect x="-183" y="-70" width="366" height="130" fill="url(#flora-fade)"/></mask>
    </defs>
  </svg>

  <!-- Sorte: Kräutermischung -->
  <div class="label label--herbs">
    <svg viewBox="-183 -183 366 366">
      <g clip-path="url(#label-clip)">
        <g role="img" aria-label="Alpenlandschaft mit Berg und See, davor Wiesenblumen: gelbe Arnika, Lavendel und Kamille">
          <rect x="-183" y="-183" width="366" height="240" fill="url(#sky-meadow)"/>
          <rect x="-183" y="-70" width="366" height="127" fill="url(#flora-herbs)" mask="url(#flora-mask)"/>
        </g>
        <rect x="-183" y="52" width="366" height="6" fill="var(--white)"/>
        <rect x="-183" y="58" width="366" height="130" fill="url(#red-band)"/>
      </g>
      <circle class="ring" r="178"/>
      <polygon class="ribbon-tail" points="-88,-88 -152,-92 -132,-80 -148,-68 -88,-70"/>
      <polygon class="ribbon-tail" points="88,-88 152,-92 132,-80 148,-68 88,-70"/>
      <path class="ribbon-band" d="M-93,-90 Q0,-78 93,-90 L93,-66 Q0,-52 -93,-66 Z"/>
      <text class="brand-name" x="0" y="-82" text-anchor="middle">Pfeffling</text>
      <text class="variety" x="0" y="-62" text-anchor="middle">Kräutermischung-Bonbons</text>
      <rect x="-30" y="26" width="60" height="60" fill="var(--white)"/>
      <rect x="-23" y="33" width="46" height="46" fill="var(--swiss-red)"/>
      <rect x="-4.5" y="43" width="9" height="26" fill="var(--white)"/>
      <rect x="-13" y="51.5" width="26" height="9" fill="var(--white)"/>
      <text class="claim" x="0" y="103" text-anchor="middle">Traditional Swiss Formula</text>
    </svg>
  </div>

  <!-- Sorte: Zitrone/Ingwer -->
  <div class="label label--lemon">
    <svg viewBox="-183 -183 366 366">
      <g clip-path="url(#label-clip)">
        <g role="img" aria-label="Alpenlandschaft mit Berg und See, umrahmt von Zitronenzweigen mit gelben Früchten und Ingwerblättern">
          <rect x="-183" y="-183" width="366" height="240" fill="url(#sky-meadow)"/>
          <rect x="-183" y="-70" width="366" height="127" fill="url(#flora-lemon)" mask="url(#flora-mask)"/>
        </g>
        <rect x="-183" y="52" width="366" height="6" fill="var(--white)"/>
        <rect x="-183" y="58" width="366" height="130" fill="url(#red-band)"/>
      </g>
      <circle class="ring" r="178"/>
      <polygon class="ribbon-tail" points="-88,-88 -152,-92 -132,-80 -148,-68 -88,-70"/>
      <polygon class="ribbon-tail" points="88,-88 152,-92 132,-80 148,-68 88,-70"/>
      <path class="ribbon-band" d="M-93,-90 Q0,-78 93,-90 L93,-66 Q0,-52 -93,-66 Z"/>
      <text class="brand-name" x="0" y="-82" text-anchor="middle">Pfeffling</text>
      <text class="variety" x="0" y="-62" text-anchor="middle">Zitrone/Ingwer-Bonbons</text>
      <rect x="-30" y="26" width="60" height="60" fill="var(--white)"/>
      <rect x="-23" y="33" width="46" height="46" fill="var(--swiss-red)"/>
      <rect x="-4.5" y="43" width="9" height="26" fill="var(--white)"/>
      <rect x="-13" y="51.5" width="26" height="9" fill="var(--white)"/>
      <text class="claim" x="0" y="103" text-anchor="middle">Traditional Swiss Formula</text>
    </svg>
  </div>

  <!-- Sorte: Anis -->
  <div class="label label--anise">
    <svg viewBox="-183 -183 366 366">
      <g clip-path="url(#label-clip)">
        <g role="img" aria-label="Alpenlandschaft mit Berg und See, davor blühende weiße Anisdolden an grünen Stängeln">
          <rect x="-183" y="-183" width="366" height="240" fill="url(#sky-meadow)"/>
          <rect x="-183" y="-70" width="366" height="127" fill="url(#flora-anise)" mask="url(#flora-mask)"/>
        </g>
        <rect x="-183" y="52" width="366" height="6" fill="var(--white)"/>
        <rect x="-183" y="58" width="366" height="130" fill="url(#red-band)"/>
      </g>
      <circle class="ring" r="178"/>
      <polygon class="ribbon-tail" points="-88,-88 -152,-92 -132,-80 -148,-68 -88,-70"/>
      <polygon class="ribbon-tail" points="88,-88 152,-92 132,-80 148,-68 88,-70"/>
      <path class="ribbon-band" d="M-93,-90 Q0,-78 93,-90 L93,-66 Q0,-52 -93,-66 Z"/>
      <text class="brand-name" x="0" y="-82" text-anchor="middle">Pfeffling</text>
      <text class="variety" x="0" y="-62" text-anchor="middle">Anis-Bonbons</text>
      <rect x="-30" y="26" width="60" height="60" fill="var(--white)"/>
      <rect x="-23" y="33" width="46" height="46" fill="var(--swiss-red)"/>
      <rect x="-4.5" y="43" width="9" height="26" fill="var(--white)"/>
      <rect x="-13" y="51.5" width="26" height="9" fill="var(--white)"/>
      <text class="claim" x="0" y="103" text-anchor="middle">Traditional Swiss Formula</text>
    </svg>
  </div>

  <!-- Sorte: Salbei -->
  <div class="label label--sage">
    <svg viewBox="-183 -183 366 366">
      <g clip-path="url(#label-clip)">
        <g role="img" aria-label="Alpenlandschaft mit Berg und See, davor eine Reihe blühender violetter Salbeipflanzen">
          <rect x="-183" y="-183" width="366" height="240" fill="url(#sky-meadow)"/>
          <rect x="-183" y="-70" width="366" height="127" fill="url(#flora-sage)" mask="url(#flora-mask)"/>
        </g>
        <rect x="-183" y="52" width="366" height="6" fill="var(--white)"/>
        <rect x="-183" y="58" width="366" height="130" fill="url(#red-band)"/>
      </g>
      <circle class="ring" r="178"/>
      <polygon class="ribbon-tail" points="-88,-88 -152,-92 -132,-80 -148,-68 -88,-70"/>
      <polygon class="ribbon-tail" points="88,-88 152,-92 132,-80 148,-68 88,-70"/>
      <path class="ribbon-band" d="M-93,-90 Q0,-78 93,-90 L93,-66 Q0,-52 -93,-66 Z"/>
      <text class="brand-name" x="0" y="-82" text-anchor="middle">Pfeffling</text>
      <text class="variety" x="0" y="-62" text-anchor="middle">Salbei-Bonbons</text>
      <rect x="-30" y="26" width="60" height="60" fill="var(--white)"/>
      <rect x="-23" y="33" width="46" height="46" fill="var(--swiss-red)"/>
      <rect x="-4.5" y="43" width="9" height="26" fill="var(--white)"/>
      <rect x="-13" y="51.5" width="26" height="9" fill="var(--white)"/>
      <text class="claim" x="0" y="103" text-anchor="middle">Traditional Swiss Formula</text>
    </svg>
  </div>

</main>
</body>
</html>
```